varnuko.com car care product labeling with cut outs will be printed on holographic sheet.

Need to make label for eco-friendly car care products. no hazard signs.
clean and simple design minimalism
wheel cleaner
tire shiner
glass cleaner
all purpose cleaner
247x90mm
166x150mm

Target Market(s)

eco friendly car care products. europe , uae

Industry/Entity Type

car care products, eco-friendly product line

Requirements
Must have
• BW design print on holographic sheet/label .eco-friendly signs
Nice to have
• premium product look and simplicity will be at first place, can be with cut outs

```html
<!DOCTYPE html>
<html lang="en">
<head>
<meta charset="UTF-8">
<title>varnuko glass cleaner label</title>
<link href="https://fonts.googleapis.com/css2?family=Montserrat:wght@400;500;600;700&display=swap" rel="stylesheet">
<style>
  :root {
    --page-bg: #ffffff;
    --ink: #1b1b1d;
    --holo-silver: #d9dde3;
    --holo-blue: #a9b7d3;
    --holo-cream: #f3f3df;
    --holo-pink: #e9cbd6;
    --holo-lilac: #d7d3e6;
    --holo-mint: #e6efe9;
    --holo-steel: #b9c2cf;
  }
  html, body {
    margin: 0;
    padding: 0;
    width: 1111px;
    height: 1200px;
    overflow: hidden;
    background: var(--page-bg);
  }
  .label {
    position: absolute;
    left: 205px;
    top: 80px;
    width: 700px;
    height: 1040px;
    font-family: "Montserrat", sans-serif;
    color: var(--ink);
    background:
      conic-gradient(from 15deg at 50% 58%,
        var(--holo-silver), var(--holo-lilac), var(--holo-steel), var(--holo-pink),
        var(--holo-cream), var(--holo-mint), var(--holo-blue), var(--holo-silver),
        var(--holo-cream), var(--holo-pink), var(--holo-lilac), var(--holo-steel),
        var(--holo-mint), var(--holo-blue), var(--holo-silver));
    overflow: hidden;
  }
  .brand {
    position: absolute;
    right: 70px;
    top: 150px;
    margin: 0;
    font-size: 104px;
    font-weight: 600;
    letter-spacing: -1px;
    line-height: 1;
  }
  .eco-badge {
    position: absolute;
    right: 70px;
    top: 640px;
    width: 150px;
    height: 150px;
  }
  .product-name {
    position: absolute;
    right: 70px;
    top: 800px;
    margin: 0;
    font-size: 70px;
    line-height: 1;
    letter-spacing: -0.5px;
  }
  .product-name .kind { font-weight: 500; }
  .product-name .type { font-weight: 700; }
  .volume {
    position: absolute;
    right: 70px;
    top: 895px;
    margin: 0;
    font-size: 30px;
    font-weight: 400;
  }
</style>
</head>
<body>
  <main class="label">
    <h1 class="brand">varnuko</h1>
    <svg class="eco-badge" viewBox="0 0 150 150" role="img" aria-label="Eco-friendly certification badge">
      <circle cx="75" cy="75" r="70" fill="none" stroke="var(--ink)" stroke-width="3"/>
      <circle cx="75" cy="75" r="46" fill="var(--ink)"/>
    </svg>
    <h2 class="product-name"><span class="kind">glass</span> <span class="type">cleaner</span></h2>
    <p class="volume">net. wt. 200ml</p>
  </main>
</body>
</html>
```